Business Report Cover

We need a revamped quarterly report cover to send to our clients. We asset manage commercial and residential properties throughout the the United States. We use a .pdf version of a cover that we've used for years but would like a fresh updated look for 2018. The cover should include our company logo (KOL Ventures) and a photo of the property as well as the Quarter/Year of the report.

Industry/Entity Type

Business

```html
<!DOCTYPE html>
<html lang="en">
<head>
<meta charset="utf-8">
<title>KOL Ventures — 2018 Quarterly Operating Report, 1st Quarter</title>
<link rel="stylesheet" href="https://fonts.googleapis.com/css2?family=Josefin+Sans:wght@400;700&display=swap">
<style>
  :root {
    --page-bg: #e9e7e3;
    --paper: #ffffff;
    --ink: #0b0b0b;
    --brand-green: #0e7a3c;
    --photo-sky: #e4e5e7;
    --photo-mid: #b9b7b4;
    --photo-ground: #4a3f3c;
  }
  html, body {
    margin: 0;
    width: 1200px;
    height: 1200px;
    overflow: hidden;
    background: var(--page-bg);
  }
  .report-cover {
    position: absolute;
    left: 204px;
    top: 40px;
    width: 792px;
    height: 1120px;
    background: var(--paper);
    box-shadow: 0 6px 18px rgba(0,0,0,0.18);
    overflow: hidden;
    font-family: "Josefin Sans", sans-serif;
    color: var(--ink);
  }
  .cover-art {
    position: absolute;
    inset: 0;
    width: 100%;
    height: 100%;
  }
  .brand-name {
    position: absolute;
    left: 45px;
    top: 62px;
    margin: 0;
    font-size: 46px;
    font-weight: 700;
    letter-spacing: 0.5px;
    color: var(--ink);
  }
  .report-year {
    position: absolute;
    left: 436px;
    top: 752px;
    margin: 0;
    font-size: 74px;
    font-weight: 700;
    line-height: 1;
    letter-spacing: -1px;
  }
  .title-rule {
    position: absolute;
    left: 438px;
    top: 829px;
    width: 313px;
    height: 6px;
    background: var(--ink);
  }
  .report-title {
    position: absolute;
    left: 438px;
    top: 846px;
    margin: 0;
    font-size: 26px;
    font-weight: 400;
    line-height: 32px;
    text-transform: uppercase;
    letter-spacing: -0.3px;
  }
  .property-address {
    position: absolute;
    left: 438px;
    top: 1022px;
    margin: 0;
    font-style: normal;
    font-size: 17px;
    line-height: 24px;
  }
</style>
</head>
<body>
  <main class="report-cover">
    <svg class="cover-art" viewBox="0 0 978 1383" preserveAspectRatio="none">
      <defs>
        <linearGradient id="property-photo-tone" x1="0" y1="0" x2="0" y2="1">
          <stop offset="0" stop-color="var(--photo-sky)"/>
          <stop offset="0.45" stop-color="#d7d8db"/>
          <stop offset="0.62" stop-color="var(--photo-mid)"/>
          <stop offset="0.78" stop-color="#6e4b45"/>
          <stop offset="1" stop-color="var(--photo-ground)"/>
        </linearGradient>
      </defs>
      <polygon class="property-photo" role="img"
        aria-label="Photo of the property: a convenience store fuel station canopy with pumps, a brick building and a tree under a cloudy sky"
        points="0,0 978,0 288,1383 0,1383" fill="url(#property-photo-tone)"/>
      <polygon class="accent-band-green" points="978,0 978,228 671,838 558,838" fill="var(--brand-green)"/>
      <polygon class="accent-band-black" points="311,1113 420,1113 288,1383 173,1383" fill="var(--ink)"/>
    </svg>

    <h1 class="brand-name">KOL Ventures</h1>

    <p class="report-year">2018</p>
    <div class="title-rule"></div>
    <h2 class="report-title">Quarterly Operating Report<br>1st Quarter</h2>

    <address class="property-address">
      Riverside Corner Market<br>
      4120 NE Harbor Point Dr.<br>
      Lakemont, WA 98001
    </address>
  </main>
</body>
</html>
```